Corvint Property Management Vendor Recruiting Email

We need a digital flyer to email and post on Social media to attract new vendors to our website to apply to complete maintenance work on our clients homes. I have one flyer we had produced recently that we are un-happy with. It is attached.

The example given is what we do not want!! We do not want any of the pictures used from the existing one

Target Market(s)

Construction companies and handyman

Industry/Entity Type

Residential maintenance and repairs

Requirements
Must have
• Join our team as the header not become a vendor

```html
<!DOCTYPE html>
<html lang="en">
<head>
<meta charset="UTF-8">
<title>Corvint Property Management – Join Our Team</title>
<link rel="stylesheet" href="https://fonts.googleapis.com/css2?family=Josefin+Sans:wght@600;700&family=Montserrat:wght@700&display=swap">
<style>
  :root {
    --ink: #0b0d19;
    --paper: #ffffff;
    --mist: #e4e4e4;
    --violet: #9656aa;
    --wave-violet: #b071c6;
    --wave-indigo: #7a7ac4;
    --wave-blue: #4aa8e0;
    --wave-cyan: #50d5f4;
  }
  * { margin: 0; padding: 0; box-sizing: border-box; }
  html, body { width: 1000px; height: 1200px; overflow: hidden; background: var(--paper); }
  .flyer { position: relative; width: 1000px; height: 1200px; overflow: hidden; background: var(--paper); color: var(--ink); font-family: "Josefin Sans", sans-serif; }
  .flyer__shapes { position: absolute; inset: 0; width: 1000px; height: 1200px; }

  .brand { position: absolute; left: 601px; top: 196px; width: 300px; text-align: center; color: var(--paper); font-family: "Montserrat", sans-serif; font-weight: 700; font-size: 24px; line-height: 30px; letter-spacing: 3px; text-transform: uppercase; }

  .headline { position: absolute; left: 28px; top: 206px; font-family: "Montserrat", sans-serif; font-weight: 700; font-size: 78px; line-height: 90px; letter-spacing: -0.5px; }

  .perk { position: absolute; left: 34px; color: var(--paper); font-weight: 700; font-size: 20.5px; line-height: 30.5px; letter-spacing: 0.3px; }
  .perk--volume { top: 543px; }
  .perk--materials { top: 705px; }
  .perk--payment { top: 891px; }

  .requirements { position: absolute; left: 502px; top: 553px; }
  .requirements__title { font-family: "Montserrat", sans-serif; font-weight: 700; font-size: 54px; line-height: 72px; }
  .requirements__list { position: absolute; top: 241px; left: 0; width: 470px; list-style: none; }
  .requirements__item { position: absolute; left: 0; padding-left: 26px; font-weight: 600; font-size: 20px; line-height: 31px; white-space: nowrap; }
  .requirements__item svg { position: absolute; left: 2px; top: 7px; width: 15px; height: 17px; }

  .contact { position: absolute; display: flex; align-items: center; gap: 8px; color: var(--paper); }
  .contact--phone { left: 35px; top: 1110px; }
  .contact--web { left: 573px; top: 1113px; color: var(--ink); }
  .contact__icon { width: 56px; height: 54px; }
  .contact__label { font-weight: 700; font-size: 27px; line-height: 28px; }
  .contact__value { font-weight: 700; font-size: 31px; line-height: 32px; }
  .contact--web .contact__value { font-size: 16.5px; line-height: 22px; }
</style>
</head>
<body>
<main class="flyer">
  <svg class="flyer__shapes" viewBox="0 0 1512 1956" preserveAspectRatio="none" aria-hidden="true">
    <defs>
      <linearGradient id="waveGradient" x1="0" y1="0" x2="1" y2="0">
        <stop offset="0" stop-color="var(--wave-violet)"/>
        <stop offset="0.45" stop-color="var(--wave-indigo)"/>
        <stop offset="0.8" stop-color="var(--wave-blue)"/>
        <stop offset="1" stop-color="var(--wave-cyan)"/>
      </linearGradient>
      <linearGradient id="waveGradientLow" x1="0" y1="0" x2="1" y2="1">
        <stop offset="0" stop-color="var(--wave-violet)"/>
        <stop offset="0.5" stop-color="var(--wave-indigo)"/>
        <stop offset="0.8" stop-color="var(--wave-blue)"/>
        <stop offset="1" stop-color="var(--wave-cyan)"/>
      </linearGradient>
    </defs>

    <!-- top waves -->
    <path d="M0,110 C420,150 640,350 840,530 C1040,710 1250,840 1512,860 L1512,0 L0,0 Z" fill="var(--mist)"/>
    <path d="M0,84 C440,115 650,300 900,470 C1110,610 1300,690 1512,701 L1512,0 L0,0 Z" fill="url(#waveGradient)"/>
    <path d="M0,92 C420,120 620,270 840,410 C1080,560 1290,600 1512,594 L1512,0 L0,0 Z" fill="var(--paper)"/>
    <path d="M0,80 C400,100 600,230 800,370 C1020,520 1230,575 1512,566 L1512,0 L0,0 Z" fill="var(--ink)"/>

    <!-- benefit arrows -->
    <path d="M0,819 L614,819 L721,936 L614,1052 L0,1052 Z" fill="var(--violet)"/>
    <path d="M0,1107 L614,1107 L721,1223 L614,1339 L0,1339 Z" fill="var(--violet)"/>
    <path d="M0,1381 L632,1381 L739,1497 L632,1614 L0,1614 Z" fill="var(--violet)"/>

    <!-- bottom waves -->
    <path d="M0,1640 C420,1645 820,1770 1001,1956 L0,1956 Z" fill="var(--mist)"/>
    <path d="M0,1656 C410,1665 760,1790 911,1956 L0,1956 Z" fill="url(#waveGradientLow)"/>
    <path d="M0,1688 C360,1700 610,1830 752,1956 L0,1956 Z" fill="var(--paper)"/>
    <path d="M0,1700 C350,1715 590,1840 740,1956 L0,1956 Z" fill="var(--ink)"/>
  </svg>

  <div class="brand">Corvint<br>Property Management</div>

  <h1 class="headline">Join Our<br>Team As<br>The Header</h1>

  <p class="perk perk--volume">95% approval rating on all submitted<br>estimates. Guaranteed work volume.</p>
  <p class="perk perk--materials">Material purchasing program to help<br>vendors with low capital or no or<br>bad credit.</p>
  <p class="perk perk--payment">Weekly secure direct deposit with net<br>30 payement terms.</p>

  <section class="requirements">
    <h2 class="requirements__title">Requirements<br>to become a<br>Vendor</h2>
    <ul class="requirements__list">
      <li class="requirements__item" style="top:0px"><svg viewBox="0 0 15 17"><path d="M2,0 L8,0 L15,8.5 L8,17 L2,17 L9,8.5 Z" fill="var(--violet)"/></svg>Auto Insurance</li>
      <li class="requirements__item" style="top:41px"><svg viewBox="0 0 15 17"><path d="M2,0 L8,0 L15,8.5 L8,17 L2,17 L9,8.5 Z" fill="var(--violet)"/></svg>Certificate of general liability insurance</li>
      <li class="requirements__item" style="top:82px"><svg viewBox="0 0 15 17"><path d="M2,0 L8,0 L15,8.5 L8,17 L2,17 L9,8.5 Z" fill="var(--violet)"/></svg>Workman’s compensation or state issued<br>exemption letter</li>
      <li class="requirements__item" style="top:153px"><svg viewBox="0 0 15 17"><path d="M2,0 L8,0 L15,8.5 L8,17 L2,17 L9,8.5 Z" fill="var(--violet)"/></svg>Driving liecense or state issued ID card</li>
      <li class="requirements__item" style="top:195px"><svg viewBox="0 0 15 17"><path d="M2,0 L8,0 L15,8.5 L8,17 L2,17 L9,8.5 Z" fill="var(--violet)"/></svg>Coverage area</li>
      <li class="requirements__item" style="top:236px"><svg viewBox="0 0 15 17"><path d="M2,0 L8,0 L15,8.5 L8,17 L2,17 L9,8.5 Z" fill="var(--violet)"/></svg>Any Specialty licenses</li>
    </ul>
  </section>

  <div class="contact contact--phone">
    <svg class="contact__icon" viewBox="0 0 56 54" aria-hidden="true">
      <rect width="56" height="54" rx="8" fill="var(--paper)"/>
      <path d="M17,14 C15,15 13,17 13.5,20 C15,29 24,38 33,40.5 C36,41.3 38.5,39.5 40,37.5 L41,36 C41.5,35 41,34 40,33.5 L34.5,30.5 C33.5,30 32.5,30.3 32,31 L30,33.5 C26,31.5 22.5,28 20.5,24 L23,22 C23.8,21.4 24,20.4 23.5,19.5 L20.5,14 C20,13 18.5,13 17.5,13.5 Z" fill="var(--ink)"/>
    </svg>
    <div>
      <div class="contact__label">Contact Us</div>
      <div class="contact__value">555-208-3146</div>
    </div>
  </div>

  <div class="contact contact--web">
    <svg class="contact__icon" viewBox="0 0 56 54" aria-hidden="true">
      <rect width="56" height="54" rx="8" fill="var(--ink)"/>
      <g fill="none" stroke="var(--paper)" stroke-width="2.4">
        <circle cx="28" cy="27" r="16"/>
        <ellipse cx="28" cy="27" rx="7" ry="16"/>
        <line x1="28" y1="11" x2="28" y2="43"/>
        <line x1="12" y1="27" x2="44" y2="27"/>
        <path d="M15,19 H41 M15,35 H41"/>
      </g>
    </svg>
    <div>
      <div class="contact__label">Visit Our Website</div>
      <div class="contact__value">www.corvintpropertymanagement.com</div>
    </div>
  </div>
</main>
</body>
</html>
```